Clearpath Ledger Billing Company Business card

Need a business card that stands out that includes name of company,(above) Owners name Marisol Whitfield phone#555-314-7762 email# ClearpathLedgerBC@mailbox-example.com and website www.Clearpathledgerbillingcompany-example.com. This is a medical billing company so the card has to relate to that or relate to steady cashflow

```html
<!DOCTYPE html>
<html lang="en">
<head>
<meta charset="utf-8">
<title>Clearpath Ledger Billing Company – Business Card</title>
<link rel="stylesheet" href="https://fonts.googleapis.com/css2?family=Arimo:wght@400;700&display=swap">
<style>
  :root {
    --stage: #2b2b2d;
    --blue-light: #1b8dc4;
    --blue-dark: #16628f;
    --navy: #134c8a;
    --green: #7cb940;
    --paper-top: #ffffff;
    --paper-bottom: #e6e6e6;
    --white: #ffffff;
  }
  * { box-sizing: border-box; margin: 0; padding: 0; }
  html, body {
    width: 1200px; height: 900px; overflow: hidden;
    background: var(--stage);
    font-family: "Arimo", Arial, sans-serif;
  }
  .canvas {
    position: relative; width: 1200px; height: 900px;
  }
  .card {
    position: absolute; left: 250px; width: 700px; height: 400px;
    border-radius: 26px; overflow: hidden;
  }
  /* Front side */
  .card-front {
    top: 35px;
    background: radial-gradient(ellipse at 55% 40%, var(--blue-light) 0%, var(--blue-dark) 85%);
    color: var(--white);
  }
  .front-brand {
    position: absolute; left: 0; right: 0; top: 150px;
    display: flex; align-items: center; justify-content: center; gap: 14px;
  }
  .brand-square {
    width: 22px; height: 22px; background: var(--green);
  }
  .front-brand-name {
    font-size: 30px; font-weight: 700; letter-spacing: 1px; color: var(--white);
  }
  .front-web {
    position: absolute; right: 40px; bottom: 34px;
    font-size: 19px; color: var(--white);
  }
  /* Back side */
  .card-back {
    top: 465px;
    background: linear-gradient(180deg, var(--paper-top) 0%, var(--paper-bottom) 100%);
    color: var(--navy);
  }
  .back-brand {
    position: absolute; left: 40px; top: 48px;
    display: flex; align-items: center; gap: 12px;
  }
  .back-brand .brand-square { width: 18px; height: 18px; background: var(--navy); }
  .back-brand-name {
    font-size: 22px; font-weight: 700; letter-spacing: 1px; color: var(--navy);
    text-transform: uppercase; line-height: 1.25;
  }
  .address {
    position: absolute; right: 40px; top: 150px; text-align: left;
    font-size: 16px; line-height: 1.3; color: var(--navy);
  }
  .person {
    position: absolute; left: 40px; top: 190px;
  }
  .person-name { font-size: 22px; font-weight: 700; color: var(--navy); }
  .person-role { font-size: 16px; color: var(--green); margin: 4px 0 16px 12px; }
  .contact {
    display: flex; align-items: center; gap: 12px;
    font-size: 17px; color: var(--navy); margin-bottom: 10px;
  }
  .contact svg { width: 20px; height: 20px; flex: none; }
  .back-band {
    position: absolute; left: 0; right: 0; bottom: 0; height: 62px;
    background: var(--navy);
    display: flex; align-items: center; justify-content: center;
    font-size: 19px; color: var(--white);
  }
</style>
</head>
<body>
<main class="canvas">
  <section class="card card-front" aria-label="Card front">
    <div class="front-brand">
      <span class="brand-square"></span>
      <span class="front-brand-name">Clearpath Ledger Billing Company</span>
    </div>
    <p class="front-web">www.Clearpathledgerbillingcompany-example.com</p>
  </section>

  <section class="card card-back" aria-label="Card back">
    <div class="back-brand">
      <span class="brand-square"></span>
      <span class="back-brand-name">Clearpath Ledger<br>Billing Company</span>
    </div>
    <p class="address">4870 Harrow Lane , Milford Delaware<br>United States 19963</p>
    <div class="person">
      <p class="person-name">Marisol Whitfield</p>
      <p class="person-role">Owner</p>
      <p class="contact">
        <svg viewBox="0 0 20 20" aria-hidden="true">
          <circle cx="10" cy="10" r="8.5" fill="none" stroke="#7cb940" stroke-width="1.6"/>
          <path d="M7 5.5l1.6 2.4-1 1.1c.6 1.3 1.5 2.2 2.8 2.8l1.1-1 2.4 1.6-.8 1.6c-3.6-.3-6.5-3.2-6.8-6.8z" fill="#7cb940"/>
        </svg>
        555-314-7762
      </p>
      <p class="contact">
        <svg viewBox="0 0 20 20" aria-hidden="true">
          <rect x="2" y="4.5" width="16" height="11" fill="none" stroke="#7cb940" stroke-width="1.5"/>
          <path d="M2 4.5l8 6.5 8-6.5M2 15.5l6-5M18 15.5l-6-5" fill="none" stroke="#7cb940" stroke-width="1.3"/>
        </svg>
        ClearpathLedgerBC@mailbox-example.com
      </p>
    </div>
    <div class="back-band">www.Clearpathledgerbillingcompany-example.com</div>
  </section>
</main>
</body>
</html>
```